Targeted Marketing

Postcard will be sent to customers who’ve already been contacted or will be in the next week or two reiterating information found on my website www.pinevaleminerals.example. Trying to keep my company name in the forefront of their mind when it comes time to divest their mineral interests.

```html
<!DOCTYPE html>
<html lang="en">
<head>
<meta charset="utf-8">
<title>Pinevale Minerals Postcard</title>
<link rel="stylesheet" href="https://fonts.googleapis.com/css2?family=Source+Sans+3:wght@400;600&family=Roboto:wght@400;500;700;900&family=Oswald:wght@500&display=swap">
<style>
:root{
  --stage:#5c5958;
  --red:#d7261e;
  --red-deep:#c81f1b;
  --black:#0b0b0b;
  --white:#ffffff;
  --ink:#111111;
  --rule:#e4e4e4;
  --stamp:#e6e2e3;
}
*{margin:0;padding:0;box-sizing:border-box}
html,body{width:1200px;height:1200px;overflow:hidden;background:var(--stage)}
.card{position:absolute;left:210px;width:780px;height:519px;background:var(--white);overflow:hidden;box-shadow:0 2px 6px rgba(0,0,0,.35)}
.card-front{top:65px}
.card-back{top:626px}
.shapes{position:absolute;inset:0}
.brand{position:absolute;left:38px;top:38px;display:flex;align-items:center;gap:12px}
.brand-mark{width:30px;height:30px;background:var(--red)}
.brand-name{font-family:"Roboto",sans-serif;font-weight:900;font-size:27px;color:var(--ink);letter-spacing:-.5px}
.heading{position:absolute;left:24px;font-family:"Roboto",sans-serif;font-weight:400;font-size:14.5px;color:var(--white);letter-spacing:.4px;word-spacing:2px}
.heading u{text-underline-offset:3px;text-decoration-thickness:1px}
.about{position:absolute;left:24px;top:178px;font-family:"Source Sans 3",sans-serif;font-size:10.2px;line-height:13px;color:var(--white);white-space:nowrap}
.about p+p{margin-top:13px}
.phone{position:absolute;left:24px;top:333px;display:flex;align-items:center;gap:8px;font-family:"Oswald",sans-serif;font-size:24px;color:var(--white)}
.contact{position:absolute;left:29px;font-family:"Roboto",sans-serif;font-size:8.8px;color:var(--white);display:flex;align-items:center;gap:9px}
.address{position:absolute;left:28px;top:443px;display:flex;gap:7px;font-family:"Roboto",sans-serif;font-size:8.8px;line-height:11.6px;color:var(--white)}
.checklist{position:absolute;list-style:none;font-family:"Source Sans 3",sans-serif;font-size:10.2px;line-height:13px;color:var(--white);white-space:nowrap}
.checklist li{display:flex;align-items:center;gap:6px}
.mail-address{position:absolute;left:397px;top:65px;font-family:"Roboto",sans-serif;font-size:8.8px;line-height:11.6px;color:var(--ink)}
.stamp-box{position:absolute;left:679px;top:46px;width:58px;height:70px;background:var(--stamp)}
.address-line{position:absolute;left:442px;width:297px;height:1px;background:var(--rule)}
</style>
</head>
<body>

<section class="card card-front">
  <svg class="shapes" viewBox="0 0 780 519" width="780" height="519">
    <defs>
      <linearGradient id="fieldTones" x1="0" y1="0" x2="0" y2="1">
        <stop offset="0" stop-color="#6f93cf"/>
        <stop offset=".55" stop-color="#dfe6ef"/>
        <stop offset=".78" stop-color="#b9ab97"/>
        <stop offset="1" stop-color="#a58a6c"/>
      </linearGradient>
    </defs>
    <polygon points="382,0 780,0 780,519 211,519" fill="url(#fieldTones)" role="img" aria-label="Photo of a red oil pumpjack on a dirt well pad under a blue cloudy sky"/>
    <polygon points="0,110 346,110 278,317 0,317" fill="var(--red)"/>
    <polygon points="0,317 278,317 242,426 0,426" fill="var(--black)"/>
    <polygon points="0,426 242,426 218,499 0,499" fill="var(--red)"/>
    <polygon points="0,499 218,499 211,519 0,519" fill="var(--black)"/>
  </svg>

  <div class="brand"><span class="brand-mark"></span><span class="brand-name">Pinevale Minerals</span></div>

  <h2 class="heading" style="top:141px">WHO WE <u>ARE:&nbsp;&nbsp;</u></h2>
  <div class="about">
    <p>Pinevale Minerals LLC is a privately-owned group of<br>experienced, trusted specialists in acquiring producing and<br>non-producing mineral and royalty interests as well as<br>overriding royalties. We offer fair, knowledgeable assistance to<br>clients interested in converting their mineral rights into cash.</p>
    <p>Pinevale is committed to industry-leading customer service.<br>We can offer you a hassle-free closing process and<br>competitive, fair-market prices.</p>
  </div>

  <div class="phone">
    <svg width="18" height="30" viewBox="0 0 18 30"><path d="M9 1c-5 2-7 7-7 14s2 12 7 14l3-6-3-2c-1-2-1-10 0-12l3-2-3-6z" fill="none" stroke="#fff" stroke-width="1.8"/></svg>
    555.014.2290
  </div>
  <div class="contact" style="top:380px">
    <svg width="13" height="9" viewBox="0 0 13 9"><rect x=".5" y=".5" width="12" height="8" fill="none" stroke="#fff"/><path d="M.5 .5l6 4.5 6-4.5M.5 8.5l4.5-4M12.5 8.5l-4.5-4" fill="none" stroke="#fff" stroke-width=".8"/></svg>
    dale@pinevaleminerals.example
  </div>
  <div class="contact" style="top:397px">
    <svg width="13" height="13" viewBox="0 0 13 13"><circle cx="6.5" cy="6.5" r="5.8" fill="none" stroke="#fff" stroke-width=".9"/><ellipse cx="6.5" cy="6.5" rx="2.6" ry="5.8" fill="none" stroke="#fff" stroke-width=".8"/><path d="M.7 6.5h11.6M1.6 3.5h9.8M1.6 9.5h9.8" stroke="#fff" stroke-width=".8"/></svg>
    www.pinevaleminerals.example
  </div>

  <div class="address">
    <svg width="10" height="14" viewBox="0 0 10 14"><path d="M5 0a5 5 0 0 0-5 5c0 4 5 9 5 9s5-5 5-9a5 5 0 0 0-5-5z" fill="#111"/><circle cx="5" cy="5" r="1.8" fill="var(--red)"/></svg>
    <div>Pinevale Minerals LLC<br>Attn: Dale M. Hartwell<br>PO Box 4410<br>Cedar Flats, NM 88000</div>
  </div>
</section>

<section class="card card-back">
  <svg class="shapes" viewBox="0 0 780 519" width="780" height="519">
    <defs>
      <linearGradient id="siteTones" x1="0" y1="0" x2="1" y2="0">
        <stop offset="0" stop-color="#9aa3ab"/>
        <stop offset=".5" stop-color="#c9b98a"/>
        <stop offset="1" stop-color="#a7b6c8"/>
      </linearGradient>
    </defs>
    <polygon points="0,0 378,0 371,20 0,20" fill="var(--red-deep)"/>
    <polygon points="0,110 343,110 276,317 0,317" fill="var(--red)"/>
    <polygon points="0,317 276,317 242,426 0,426" fill="var(--black)"/>
    <polygon points="0,426 242,426 218,499 0,499" fill="url(#siteTones)" role="img" aria-label="Photo of heavy machinery and a steel pipe at an oilfield work site"/>
    <polygon points="0,499 218,499 211,519 0,519" fill="var(--black)"/>
  </svg>

  <div class="brand"><span class="brand-mark"></span><span class="brand-name">Pinevale Minerals</span></div>

  <h2 class="heading" style="top:137px">WHY <u>SELL:</u></h2>
  <ul class="checklist" style="left:34px;top:164px">
    <li><svg width="9" height="9" viewBox="0 0 9 9"><path d="M1 5l2.5 3L8 1" fill="none" stroke="#fff" stroke-width="1.8"/></svg>Immediate Cash</li>
    <li><svg width="9" height="9" viewBox="0 0 9 9"><path d="M1 5l2.5 3L8 1" fill="none" stroke="#fff" stroke-width="1.8"/></svg>Monthly Revenue Stream</li>
    <li><svg width="9" height="9" viewBox="0 0 9 9"><path d="M1 5l2.5 3L8 1" fill="none" stroke="#fff" stroke-width="1.8"/></svg>Estate Planning</li>
  </ul>
  <ul class="checklist" style="left:179px;top:164px">
    <li><svg width="9" height="9" viewBox="0 0 9 9"><path d="M1 5l2.5 3L8 1" fill="none" stroke="#fff" stroke-width="1.8"/></svg>Tax Reasons</li>
    <li><svg width="9" height="9" viewBox="0 0 9 9"><path d="M1 5l2.5 3L8 1" fill="none" stroke="#fff" stroke-width="1.8"/></svg>Risk</li>
    <li><svg width="9" height="9" viewBox="0 0 9 9"><path d="M1 5l2.5 3L8 1" fill="none" stroke="#fff" stroke-width="1.8"/></svg>Management</li>
  </ul>

  <h2 class="heading" style="top:228px">HOW WE <u>VALUE</u>:</h2>
  <ul class="checklist" style="left:34px;top:255px">
    <li><svg width="9" height="9" viewBox="0 0 9 9"><path d="M1 5l2.5 3L8 1" fill="none" stroke="#fff" stroke-width="1.8"/></svg>Historical Production</li>
    <li><svg width="9" height="9" viewBox="0 0 9 9"><path d="M1 5l2.5 3L8 1" fill="none" stroke="#fff" stroke-width="1.8"/></svg>Reservoir Analysis</li>
    <li><svg width="9" height="9" viewBox="0 0 9 9"><path d="M1 5l2.5 3L8 1" fill="none" stroke="#fff" stroke-width="1.8"/></svg>Operator Reputation</li>
  </ul>
  <ul class="checklist" style="left:179px;top:255px">
    <li><svg width="9" height="9" viewBox="0 0 9 9"><path d="M1 5l2.5 3L8 1" fill="none" stroke="#fff" stroke-width="1.8"/></svg>Future Drilling</li>
    <li><svg width="9" height="9" viewBox="0 0 9 9"><path d="M1 5l2.5 3L8 1" fill="none" stroke="#fff" stroke-width="1.8"/></svg>Commodity Pricing</li>
  </ul>

  <div class="phone">
    <svg width="18" height="30" viewBox="0 0 18 30"><path d="M9 1c-5 2-7 7-7 14s2 12 7 14l3-6-3-2c-1-2-1-10 0-12l3-2-3-6z" fill="none" stroke="#fff" stroke-width="1.8"/></svg>
    555.014.2290
  </div>
  <div class="contact" style="top:380px">
    <svg width="13" height="9" viewBox="0 0 13 9"><rect x=".5" y=".5" width="12" height="8" fill="none" stroke="#fff"/><path d="M.5 .5l6 4.5 6-4.5M.5 8.5l4.5-4M12.5 8.5l-4.5-4" fill="none" stroke="#fff" stroke-width=".8"/></svg>
    dale@pinevaleminerals.example
  </div>
  <div class="contact" style="top:397px">
    <svg width="13" height="13" viewBox="0 0 13 13"><circle cx="6.5" cy="6.5" r="5.8" fill="none" stroke="#fff" stroke-width=".9"/><ellipse cx="6.5" cy="6.5" rx="2.6" ry="5.8" fill="none" stroke="#fff" stroke-width=".8"/><path d="M.7 6.5h11.6M1.6 3.5h9.8M1.6 9.5h9.8" stroke="#fff" stroke-width=".8"/></svg>
    www.pinevaleminerals.example
  </div>

  <div class="mail-address">Pinevale Minerals LLC<br>Attn: Dale M. Hartwell<br>PO Box 4410<br>Cedar Flats, NM 88000</div>
  <div class="stamp-box"></div>
  <div class="address-line" style="top:187px"></div>
  <div class="address-line" style="top:238px"></div>
  <div class="address-line" style="top:288px"></div>
  <div class="address-line" style="top:342px"></div>
</section>

</body>
</html>
```